Cards and what not
Project: Stationary
Stationary - Consulting
Stationary
Simple
Tomaso Reyk Halden
CEO
Do not want to use an address please.
833-LUMACORP (833-586-2267)
th@lumacorp.com
www.lumacorp.com
Please make the font large enough to more easily read. Some cards...the font is too small. Please use our logo as well. I prefer a vertical design but open to horizontal too. Many thanks :)
lumacorp lumacorp
I am looking for a vertical design while open to checking out horizontal designs (for the business card). Thanks guys (and ladies)

```html
<!DOCTYPE html>
<html lang="en">
<head>
<meta charset="utf-8">
<title>Lumacorp Business Card</title>
<link href="https://fonts.googleapis.com/css2?family=Open+Sans:wght@400;600;700&display=swap" rel="stylesheet">
<style>
  :root{
    --bg:#e4e5e7;
    --card:#ffffff;
    --accent:#3fc3d9;
    --accent-dark:#2aa9c0;
    --ink:#3a3d40;
    --muted:#6f7377;
    --rule:#c9ccd0;
  }
  *{margin:0;padding:0;box-sizing:border-box}
  html,body{width:1200px;height:883px;overflow:hidden}
  body{
    background:var(--bg);
    font-family:'Open Sans',sans-serif;
    position:relative;
  }
  .card{
    position:absolute;
    width:520px;height:300px;
    background:var(--card);
    border-radius:22px;
    overflow:hidden;
    box-shadow:0 6px 18px rgba(0,0,0,.12);
  }
  .card--back{left:620px;top:110px}
  .card--front{left:80px;top:440px}

  .brand{
    position:absolute;
    display:flex;align-items:center;gap:10px;
    color:var(--accent);
    font-weight:600;
    letter-spacing:2px;
    text-transform:uppercase;
    white-space:nowrap;
  }
  .brand-dot{
    width:16px;height:16px;border-radius:50%;
    background:var(--accent);
  }
  .card--back .brand{left:50%;top:50%;transform:translate(-50%,-50%);font-size:36px}
  .card--front .brand{left:230px;top:34px;font-size:32px}

  .person{position:absolute;left:28px;top:98px}
  .person-name{font-size:17px;font-weight:700;color:var(--ink);text-transform:uppercase;letter-spacing:.5px;line-height:1.3}
  .person-title{font-size:14px;color:var(--muted);margin-top:2px}

  .contact{position:absolute;left:28px;top:152px;list-style:none}
  .contact li{
    display:flex;align-items:center;gap:9px;
    font-size:14px;color:var(--ink);
    height:24px;
    white-space:nowrap;
  }
  .contact svg{width:12px;height:12px;fill:var(--accent-dark);flex:none}
  .contact .icon-mail{fill:none;stroke:var(--accent-dark);stroke-width:1.2}

  .band{position:absolute;left:0;bottom:0;width:520px;height:60px}
</style>
</head>
<body>

  <section class="card card--back" aria-label="Card back">
    <div class="brand"><span class="brand-dot"></span>Lumacorp</div>
  </section>

  <section class="card card--front" aria-label="Card front">
    <svg class="band" viewBox="0 0 520 60" preserveAspectRatio="none" aria-hidden="true">
      <path d="M0 8 Q40 40 180 42 L520 42 L520 47 L180 47 Q30 46 0 14 Z" fill="var(--rule)"/>
      <path d="M150 47 L520 47 L520 60 L0 60 L0 38 Q40 47 150 47 Z" fill="var(--accent)"/>
    </svg>

    <div class="brand"><span class="brand-dot"></span>Lumacorp</div>

    <div class="person">
      <p class="person-name">Tomaso Reyk Halden</p>
      <p class="person-title">CEO</p>
    </div>

    <ul class="contact">
      <li><svg viewBox="0 0 10 10"><path d="M2 0h2l1 3-1.5 1a6 6 0 0 0 2.5 2.5L7 5l3 1v2a2 2 0 0 1-2 2A8 8 0 0 1 0 2a2 2 0 0 1 2-2z"/></svg>833-LUMACORP (833-586-2267)</li>
      <li><svg class="icon-mail" viewBox="0 0 10 10"><path d="M0.6 2.2h8.8v5.6H0.6z M0.6 2.2l4.4 3.2 4.4-3.2"/></svg>th@lumacorp.com</li>
      <li><svg viewBox="0 0 10 10"><circle cx="5" cy="5" r="5"/></svg>www.lumacorp.com</li>
    </ul>
  </section>

</body>
</html>
```